Digital Marketing Online Shop Needs a Home Page Web Design

Here is some background on the new home page and the message we want to relay to people visiting our site.
The new site design will be very similar to the following sites
http://trellisoft.com/
https://quillhaven.com/
http://brightmarrow.io/
http://sketchotter.com/
http://clipharbor.com/
We are a small marketing agency of 3 and we have built up and impressive contact list of partners over the last 16 years to help our customers take their digital marketing to the next level.
The four core areas of products we will be promoting and selling through our online shop are the following :
Web design
Content marketing
Graphic design
Coaching
We operate our agency in a new way, not the old school way so our customers can receive on-demand marketing.
We plan to have an online shop so visitors can purchase some of our services, very similar to how Quill Haven and Sketch Otter offer their services.
In the end, we want the same call to action layout as Trellisoft, Quill Haven and Sketch Otter, however, since we are an agency we would like to blend in Bright Marrow's layout.
We want the customer to either contact us about our services or purchase one of the services from our shop.
We are trying to make the whole digital marketing experience more transactional like retail and not so traditional servicey. :-)
It is from our years of experience and finding the right partners that allows us to offer this type of solution to businesses in the Maritime Provinces (New Brunswick, Nova Scotia, Prince Edward Island, Canada).
Also, because we are offering more of an on-demand/self serve option and we have lower overhead, we hope to pass along great pricing to our customers for their marketing needs. We really want this offer to expand outside of our local market in Saint John, New Brunswick.
I would also like to have a call to action written for a hero image at the top of the page, like the Trellisoft site.
After that I would like the content to flow through similar to Quill Haven & Trellisoft. But mix in some of the agency like content you see with Clipharbor, Bright Marrow.
I have also included the first draft of the content for our home page.
Menu Items will be About, How We Work, Learn, Shop, Contact
Please let me know if you need anything else.
Target Market(s)
Small businesses, 1-10 person companies with up to 5 million in revenue. Mostly service companies, but some retail.
Industry/Entity Type
Marketing
Number of Pages Required
1 page

```html
<!DOCTYPE html>
<html lang="en">
<head>
<meta charset="utf-8">
<title>Harborline Digital – Home</title>
<link rel="stylesheet" href="https://fonts.googleapis.com/css2?family=Roboto:wght@300;400;500&display=swap">
<style>
:root{
  --blue:#2777c5;
  --blue-dark:#2266ad;
  --navy:#1b4f8f;
  --green:#6fcc04;
  --ink:#1d1d1d;
  --text:#444;
  --grey-band:#ececec;
  --white:#fff;
  --link:#2777c5;
}
*{box-sizing:border-box;margin:0;padding:0}
html,body{width:1200px;height:2287px;overflow:hidden}
body{font-family:'Roboto',Arial,sans-serif;color:var(--text);background:var(--white);position:relative}
a{text-decoration:none;color:inherit}

/* header */
.site-header{height:61px;display:flex;align-items:center;justify-content:space-between;padding:0 89px;border-bottom:1px solid #e3e3e3;background:var(--white)}
.brand{display:flex;align-items:center;gap:10px;font-size:23px;font-weight:500;color:var(--blue)}
.brand-dot{width:34px;height:34px;border-radius:50%;background:var(--blue)}
.main-nav{display:flex;align-items:center;height:61px}
.main-nav a{font-size:14px;color:#333;padding:0 20px;height:61px;display:flex;align-items:center;position:relative}
.main-nav a.is-active::after{content:"";position:absolute;left:16px;right:16px;bottom:-1px;height:3px;background:var(--navy)}
.btn-login{margin-left:8px;background:var(--navy);color:var(--white);font-size:13px;height:36px;padding:0 22px;display:flex;align-items:center;gap:8px;border-radius:3px}

/* hero */
.hero{position:relative;height:555px;overflow:hidden}
.hero-photo{position:absolute;inset:0;background:radial-gradient(ellipse at 50% 45%,#efefef 0%,#dedede 55%,#c9c9c9 100%)}
.hero-content{position:relative;text-align:center;padding-top:214px}
.hero h1{font-weight:400;font-size:34px;line-height:36px;color:var(--ink)}
.hero p{font-size:13.5px;line-height:20px;color:#555;margin:12px auto 0;width:560px}
.hero-actions{display:flex;justify-content:center;gap:14px;margin-top:16px}
.btn{display:inline-flex;align-items:center;justify-content:center;font-size:14px;height:36px;border-radius:2px}
.btn-shop{background:var(--green);color:var(--white);width:79px}
.btn-contact{border:2px solid var(--navy);color:var(--navy);width:112px}

/* features band */
.features{background:var(--blue);height:241px;display:flex;justify-content:center;gap:0;padding-top:74px}
.feature{width:320px;text-align:center;color:var(--white)}
.feature svg{width:56px;height:52px}
.feature h3{font-size:17px;font-weight:500;margin-top:8px}
.feature p{font-size:12.5px;margin-top:6px;color:#e4eefb}

/* services */
.services{height:513px;padding-top:50px}
.section-title{font-weight:400;font-size:33px;color:var(--ink);text-align:center}
.service-grid{display:grid;grid-template-columns:534px 420px;column-gap:0;margin:30px 0 0 137px;row-gap:34px}
.service{display:flex;gap:12px}
.service svg{width:36px;height:34px;flex:none;margin-top:-2px}
.service h3{font-size:20px;font-weight:400;color:var(--ink);line-height:22px}
.service p{font-size:12.5px;line-height:20px;color:#444;margin-top:6px;width:400px}
.read-more{display:block;font-size:12px;color:var(--link);margin-top:8px}
.btn-more{display:flex;margin:26px auto 0;width:142px;height:37px;border:1px solid #d6d6d6;background:var(--white);color:#333;font-size:15px;align-items:center;justify-content:center;border-radius:2px}

/* testimonials */
.testimonials{background:var(--grey-band);height:365px;padding-top:46px;text-align:center}
.avatar{width:77px;height:77px;border-radius:50%;background:linear-gradient(#b8aa9c,#7e7368);margin:14px auto 0;border:2px solid var(--white)}
.quote{position:relative;width:730px;margin:18px auto 0;font-size:15px;line-height:21px;color:#333}
.quote-mark{position:absolute;color:var(--blue);font-size:38px;font-weight:500;line-height:1;font-family:Georgia,serif}
.quote-mark.open{left:-20px;top:-10px}
.quote-mark.close{right:150px;bottom:-26px}
.author{font-size:14px;font-weight:500;color:#222;margin-top:14px;letter-spacing:.5px}
.dots{display:flex;justify-content:center;gap:6px;margin-top:18px}
.dots span{width:8px;height:8px;border-radius:50%;background:var(--white)}
.dots span.is-active{width:12px;height:12px;margin-top:-2px;background:var(--blue)}

/* partners + cta */
.partners{height:281px;text-align:center;padding-top:57px}
.partner-row{display:flex;justify-content:space-between;padding:0 118px;align-items:center}
.partner-badge{width:140px;height:50px;border-radius:4px;background:#eef1f5}
.btn-start{display:flex;margin:48px auto 0;width:244px;height:49px;background:var(--green);color:var(--white);font-size:18px;align-items:center;justify-content:center;gap:10px;border-radius:2px}
.signin{font-size:14.5px;margin-top:14px;color:#333}
.signin a{color:var(--link)}

/* newsletter */
.newsletter{background:var(--blue);height:221px;text-align:center;padding-top:42px;color:var(--white)}
.newsletter h2{font-weight:400;font-size:25px}
.subscribe-form{display:flex;justify-content:center;margin-top:18px}
.subscribe-form .field{width:395px;height:45px;background:var(--white);color:#333;font-size:13px;display:flex;align-items:center;padding-left:14px;border-radius:3px 0 0 3px;text-align:left}
.subscribe-form .submit{width:149px;height:45px;background:var(--green);display:flex;align-items:center;justify-content:center;font-size:15px;border-radius:0 3px 3px 0}
.social{display:flex;justify-content:center;gap:13px;margin-top:22px}
.social span{width:34px;height:34px;border-radius:50%}
.social .s1{background:#3b5a99}.social .s2{background:#25a9e0}.social .s3{background:#d93a2f}.social .s4{background:#1e5a93}

/* footer */
.site-footer{background:var(--blue-dark);height:50px;display:flex;align-items:center;justify-content:space-between;padding:0 90px 0 88px;color:var(--white);font-size:12px}
.footer-nav{display:flex;gap:27px}
.to-top{position:absolute;left:1134px;top:2220px;width:34px;height:34px;border-radius:50%;background:var(--white);display:flex;align-items:center;justify-content:center;box-shadow:0 1px 4px rgba(0,0,0,.25)}
</style>
</head>
<body>

<header class="site-header">
  <a class="brand" href="#"><span class="brand-dot"></span>Harborline Digital</a>
  <nav class="main-nav">
    <a class="is-active" href="#">Home</a>
    <a href="#">How We Work</a>
    <a href="#">Learn</a>
    <a href="#">Shop</a>
    <a href="#">Contact</a>
    <a class="btn-login" href="#">
      <svg width="11" height="12" viewBox="0 0 11 12"><circle cx="5.5" cy="3" r="3" fill="#fff"/><path d="M0 12c0-4 2.5-5.5 5.5-5.5S11 8 11 12z" fill="#fff"/></svg>Login</a>
  </nav>
</header>

<section class="hero">
  <div class="hero-photo" role="img" aria-label="Desk scene with notebook, pen, phone and laptop on a light grey surface"></div>
  <div class="hero-content">
    <h1>Want An Online<br>Presence For Your Small Business</h1>
    <p>Give your business the exposure it deserves! Get started by ordering services directly from the shop or by shooting us an email</p>
    <div class="hero-actions">
      <a class="btn btn-shop" href="#">Shop</a>
      <a class="btn btn-contact" href="#">Conatact</a>
    </div>
  </div>
</section>

<section class="features">
  <div class="feature">
    <svg viewBox="0 0 56 52"><rect x="4" y="10" width="36" height="36" fill="none" stroke="#fff" stroke-width="4"/><path d="M12 26l10 10L50 6" fill="none" stroke="#fff" stroke-width="6"/></svg>
    <h3>Vetted Copywriters</h3>
    <p>Lorem ipsum is siply dummy text.</p>
  </div>
  <div class="feature">
    <svg viewBox="0 0 56 52"><path d="M12 26a16 16 0 0 1 28-11" fill="none" stroke="#fff" stroke-width="5"/><path d="M44 26a16 16 0 0 1-28 11" fill="none" stroke="#fff" stroke-width="5"/><path d="M36 8l8 2-2 8z" fill="#fff"/><path d="M20 44l-8-2 2-8z" fill="#fff"/><circle cx="28" cy="26" r="9" fill="#fff"/><path d="M28 20v6h5" stroke="#2777c5" stroke-width="2.5" fill="none"/></svg>
    <h3>On-Time Delivery</h3>
    <p>Lorem ipsum is siply dummy text.</p>
  </div>
  <div class="feature">
    <svg viewBox="0 0 56 52"><circle cx="28" cy="12" r="10" fill="#fff"/><path d="M10 50c0-16 7-24 18-24s18 8 18 24z" fill="#fff"/><path d="M26 27h4l1 14-3 4-3-4z" fill="#2777c5"/></svg>
    <h3>Fully Managed</h3>
    <p>Lorem ipsum is siply dummy text.</p>
  </div>
</section>

<section class="services">
  <h2 class="section-title">Our Services</h2>
  <div class="service-grid">
    <article class="service">
      <svg viewBox="0 0 36 34"><rect x="2" y="6" width="28" height="20" fill="none" stroke="#222" stroke-width="2.5"/><path d="M12 26v5h8v-5M8 31h16" stroke="#222" stroke-width="2.5" fill="none"/><path d="M14 20L32 2" stroke="#222" stroke-width="3"/></svg>
      <div><h3>Web Design</h3><p>Let's be honest. Your website is the face of your business in the modern world. When done well, it can communicate personality, expertise, and high-quality of service.</p><a class="read-more" href="#">Read More</a></div>
    </article>
    <article class="service">
      <svg viewBox="0 0 36 34"><rect x="2" y="2" width="30" height="22" rx="2" fill="none" stroke="#222" stroke-width="2.5"/><rect x="2" y="2" width="30" height="6" fill="#222"/><circle cx="20" cy="24" r="8" fill="#fff" stroke="#222" stroke-width="2.5"/><path d="M12 24h16M20 16v16" stroke="#222" stroke-width="1.5"/></svg>
      <div><h3>Content Marketing</h3><p>Content Marketing is to the 21st century what traditional adverti-sing was to the ‘60s. Thanks to the power of the internet, so many businesses have never had such access .</p><a class="read-more" href="#">Read More</a></div>
    </article>
    <article class="service">
      <svg viewBox="0 0 36 34"><rect x="2" y="4" width="30" height="20" fill="none" stroke="#222" stroke-width="2.5"/><rect x="6" y="8" width="22" height="12" fill="#222"/><path d="M12 24v5h10v-5M7 30h20" stroke="#222" stroke-width="2.5" fill="none"/></svg>
      <div><h3>Graphic Design</h3><p>Creating a consistent and eye-catching brand for your business is one of the best ways to draw in customers on the web. And nothing builds a brand like top notch graphic design.</p><a class="read-more" href="#">Read More</a></div>
    </article>
    <article class="service">
      <svg viewBox="0 0 36 34"><rect x="18" y="2" width="16" height="10" fill="#222"/><circle cx="10" cy="10" r="4" fill="#222"/><path d="M4 22c0-6 3-8 6-8s6 2 6 8z" fill="#222"/><path d="M2 24h32" stroke="#222" stroke-width="2"/><circle cx="6" cy="29" r="2.5" fill="#222"/><circle cx="14" cy="29" r="2.5" fill="#222"/><circle cx="22" cy="29" r="2.5" fill="#222"/><circle cx="30" cy="29" r="2.5" fill="#222"/></svg>
      <div><h3>Coaching</h3><p>Taking your small business to the next level can be a tricky pro-cess. Marketing jargon, confusing tools, and literally millions of resources can make expanding seem like .</p><a class="read-more" href="#">Read More</a></div>
    </article>
  </div>
  <a class="btn-more" href="#">View More</a>
</section>

<section class="testimonials">
  <h2 class="section-title">Testimonials</h2>
  <div class="avatar" role="img" aria-label="Portrait of the client quoted"></div>
  <blockquote class="quote">
    <span class="quote-mark open">“</span>
    This is Layerpad's version &nbsp;of Lorem Ipsum. Proin gravida nibh vel velit auctor aliquet. Aenean sollicitudin, lorem quis bibendum auctor, nisi elit consequat ipsum, nec sagittis sem nibh id elit. Duis sed odio sit amet nibh vulputate cursus a sit amet mauris.
    <span class="quote-mark close">”</span>
  </blockquote>
  <p class="author">JOHN / DOE</p>
  <div class="dots"><span></span><span class="is-active"></span><span></span></div>
</section>

<section class="partners">
  <div class="partner-row">
    <span class="partner-badge"></span>
    <span class="partner-badge"></span>
    <span class="partner-badge"></span>
    <span class="partner-badge"></span>
    <span class="partner-badge"></span>
  </div>
  <a class="btn-start" href="#">
    <svg width="22" height="22" viewBox="0 0 22 22"><path d="M6 5a8 8 0 1 0 10 0" fill="none" stroke="#fff" stroke-width="2.5"/><path d="M11 1v10" stroke="#fff" stroke-width="2.5"/></svg>Get Started</a>
  <p class="signin"><a href="#">Already have an account?</a> Sign In Here.</p>
</section>

<section class="newsletter">
  <h2>Subscribe to our Newsletter</h2>
  <div class="subscribe-form">
    <span class="field">Email address</span>
    <span class="submit">Subscribe</span>
  </div>
  <div class="social"><span class="s1"></span><span class="s2"></span><span class="s3"></span><span class="s4"></span></div>
</section>

<footer class="site-footer">
  <span>Copyright 2016 | All Right Reserved</span>
  <nav class="footer-nav"><a href="#">Home</a><a href="#">How We Work</a><a href="#">Learn</a><a href="#">Shop</a><a href="#">Contact</a></nav>
</footer>
<a class="to-top" href="#"><svg width="12" height="8" viewBox="0 0 12 8"><path d="M1 7l5-5 5 5" fill="none" stroke="#222" stroke-width="2"/></svg></a>

</body>
</html>
```